Copper Lane Assembly Lanterns EP Design Cover

I need a CD cover design for my EP titled "Lanterns". The theme can be either the alphabetic letters, or written letters, whichever seems best for your graphic concept.<br/><br/>Please take a listen to the tracks on tunebasin here:<br/>https://tunebasin.example/copper-lane-assembly<br/>And here:<br/>https://tunebasin.example/copper-lane-assembly/silver-morning/s-KQ7rT<br/>https://tunebasin.example/copper-lane-assembly/rain-on-the-porch-demo-mix/s-WM4PZ<br/><br/>I look forward to seeing you designs and choosing one for the EP cover.

Target Market(s)

Indie-pop/rock

Colors

Designer to choose colors to be used in the design.

Requirements
Must have
• Copper Lane Assembly Logo
• Should meet Friendloop criteria for % text to picture ratio

```html
<!DOCTYPE html>
<html lang="en">
<head>
<meta charset="utf-8">
<title>Copper Lane Assembly — Lanterns</title>
<link rel="stylesheet" href="https://fonts.googleapis.com/css2?family=Josefin+Sans:wght@600&family=Oswald:wght@300&display=swap">
<style>
  :root {
    --wood-dark: #2a140c;
    --wood-mid: #4a2416;
    --wood-warm: #6a3320;
    --paper-light: #dccfaa;
    --paper-shade: #c2b084;
    --ink-white: #ffffff;
  }
  html, body {
    margin: 0;
    padding: 0;
    overflow: hidden;
    background: var(--wood-dark);
  }
  .cover {
    position: relative;
    width: 1200px;
    height: 1200px;
    overflow: hidden;
  }
  .cover__backdrop {
    position: absolute;
    inset: 0;
    background: radial-gradient(ellipse at 62% 38%, var(--wood-warm) 0%, var(--wood-mid) 45%, var(--wood-dark) 100%);
  }
  .envelopes {
    position: absolute;
    inset: 0;
  }
  .envelope-area {
    position: absolute;
    width: 300px;
    height: 200px;
    margin: -100px 0 0 -150px;
    background: linear-gradient(180deg, var(--paper-shade) 0%, var(--paper-light) 55%);
    border-radius: 4px;
    box-shadow: 0 6px 14px rgba(0, 0, 0, 0.4);
  }
  .title {
    position: absolute;
    inset: 0;
    margin: 0;
    font-weight: normal;
  }
  .title__letter {
    position: absolute;
    width: 140px;
    height: 140px;
    margin: -70px 0 0 -70px;
    display: flex;
    align-items: center;
    justify-content: center;
    font-family: "Josefin Sans", sans-serif;
    font-weight: 600;
    font-size: 128px;
    line-height: 1;
    padding-top: 22px;
    box-sizing: border-box;
    color: var(--ink-white);
  }
  .band-name {
    position: absolute;
    left: 116px;
    top: 826px;
    margin: 0;
    font-family: "Oswald", sans-serif;
    font-weight: 300;
    font-size: 66px;
    line-height: 100px;
    letter-spacing: 2px;
    text-transform: uppercase;
    color: var(--ink-white);
  }
  .band-name span { display: block; }
</style>
</head>
<body>
<main class="cover">
  <div class="cover__backdrop" role="img" aria-label="Dark reddish-brown wooden floorboards"></div>

  <div class="envelopes" role="img" aria-label="A diagonal trail of open airmail envelopes, each holding one letter of the title">
    <div class="envelope-area" style="left:258px; top:275px; transform:rotate(-3deg);"></div>
    <div class="envelope-area" style="left:356px; top:363px; transform:rotate(8deg);"></div>
    <div class="envelope-area" style="left:454px; top:451px; transform:rotate(-4deg);"></div>
    <div class="envelope-area" style="left:552px; top:539px; transform:rotate(6deg);"></div>
    <div class="envelope-area" style="left:650px; top:627px; transform:rotate(-3deg);"></div>
    <div class="envelope-area" style="left:748px; top:715px; transform:rotate(9deg);"></div>
    <div class="envelope-area" style="left:846px; top:803px; transform:rotate(-5deg);"></div>
    <div class="envelope-area" style="left:944px; top:891px; transform:rotate(6deg);"></div>
  </div>

  <h1 class="title" aria-label="Lanterns">
    <span class="title__letter" style="left:258px; top:240px;" aria-hidden="true">L</span>
    <span class="title__letter" style="left:356px; top:328px;" aria-hidden="true">A</span>
    <span class="title__letter" style="left:454px; top:416px;" aria-hidden="true">N</span>
    <span class="title__letter" style="left:552px; top:504px;" aria-hidden="true">T</span>
    <span class="title__letter" style="left:650px; top:592px;" aria-hidden="true">E</span>
    <span class="title__letter" style="left:748px; top:680px;" aria-hidden="true">R</span>
    <span class="title__letter" style="left:846px; top:768px;" aria-hidden="true">N</span>
    <span class="title__letter" style="left:944px; top:856px;" aria-hidden="true">S</span>
  </h1>

  <p class="band-name">
    <span>Copper</span>
    <span>Lane</span>
    <span>Assembly</span>
  </p>
</main>
</body>
</html>
```